Business Consultancy Business Card Design

Business Card design required for Business Analysis and Project Consultancy business based in Scotland.

Company Name - Brackwell Consulting

Back - Company Logo

Front Details

Euan Brackwell
07402 916 254
euan.brackwell@brackwellconsulting.example
http://www.brackwellconsulting.example

Colours should match the logo colours but I am open to design ideas.

```html
<!DOCTYPE html>
<html lang="en">
<head>
<meta charset="utf-8">
<title>Brackwell Consulting – Business Cards</title>
<link href="https://fonts.googleapis.com/css2?family=Montserrat:wght@400&family=Open+Sans:wght@400;600&display=swap" rel="stylesheet">
<style>
  :root {
    --brand-blue: #009ddc;
    --brand-green: #6cb33f;
    --ink-grey: #666666;
    --rule-grey: #6d6e70;
    --paper: #ffffff;
    --canvas: #ffffff;
  }
  html, body {
    margin: 0;
    padding: 0;
    width: 1200px;
    height: 1000px;
    overflow: hidden;
    background: var(--canvas);
  }
  .canvas {
    position: relative;
    width: 1200px;
    height: 1000px;
  }
  .card {
    position: absolute;
    left: 258px;
    width: 637px;
    height: 412px;
    overflow: hidden;
    box-shadow: 4px 10px 18px rgba(0, 0, 0, 0.35);
  }
  .card--back {
    top: 62px;
    background: var(--brand-blue);
  }
  .card--front {
    top: 530px;
    background: var(--paper);
  }
  .wordmark {
    position: absolute;
    display: flex;
    align-items: center;
    font-family: "Montserrat", "Helvetica Neue", Arial, sans-serif;
    font-weight: 400;
    text-transform: uppercase;
    white-space: nowrap;
  }
  .wordmark__dot {
    border-radius: 50%;
    flex: none;
  }
  .card--back .wordmark {
    left: 64px;
    top: 182px;
    color: var(--paper);
    font-size: 31px;
    letter-spacing: 0.5px;
  }
  .card--back .wordmark__dot {
    width: 56px;
    height: 56px;
    background: var(--paper);
    margin-right: 22px;
  }
  .card--front .wordmark {
    left: 68px;
    top: 52px;
    color: var(--ink-grey);
    font-size: 23px;
  }
  .card--front .wordmark__dot {
    width: 42px;
    height: 42px;
    background: var(--brand-blue);
    margin-right: 18px;
  }
  .name-band {
    position: absolute;
    left: 124px;
    top: 142px;
    width: 513px;
    height: 75px;
    background: var(--brand-green);
    border-bottom: 7px solid var(--rule-grey);
  }
  .name-band__name {
    position: absolute;
    left: 30px;
    top: 22px;
    margin: 0;
    font-family: "Open Sans", Arial, sans-serif;
    font-weight: 400;
    font-size: 26px;
    line-height: 1.2;
    color: var(--paper);
  }
  .contact-list {
    position: absolute;
    left: 156px;
    top: 243px;
    margin: 0;
    padding: 0;
    list-style: none;
    font-family: "Open Sans", Arial, sans-serif;
    font-size: 16px;
    color: var(--ink-grey);
  }
  .contact-list__item {
    display: flex;
    align-items: center;
    height: 26px;
  }
  .contact-list__item--phone { font-weight: 600; }
  .contact-list__icon {
    width: 12px;
    height: 12px;
    margin-right: 11px;
    flex: none;
  }
  .web-bar {
    position: absolute;
    left: 124px;
    top: 366px;
    width: 513px;
    height: 46px;
    background: var(--brand-blue);
  }
  .web-bar__url {
    position: absolute;
    left: 30px;
    top: 9px;
    font-family: "Open Sans", Arial, sans-serif;
    font-size: 19px;
    letter-spacing: 4.6px;
    color: var(--paper);
    white-space: nowrap;
  }
</style>
</head>
<body>
<main class="canvas">

  <section class="card card--back" aria-label="Card back">
    <div class="wordmark">
      <span class="wordmark__dot"></span>
      <span class="wordmark__name">Brackwell Consulting</span>
    </div>
  </section>

  <section class="card card--front" aria-label="Card front">
    <div class="wordmark">
      <span class="wordmark__dot"></span>
      <span class="wordmark__name">Brackwell Consulting</span>
    </div>

    <div class="name-band">
      <h1 class="name-band__name">Euan Brackwell</h1>
    </div>

    <ul class="contact-list">
      <li class="contact-list__item contact-list__item--phone">
        <svg class="contact-list__icon" viewBox="0 0 12 12" aria-hidden="true"><circle cx="6" cy="6" r="6" fill="var(--brand-blue)"/></svg>
        07402 916 254
      </li>
      <li class="contact-list__item">
        <svg class="contact-list__icon" viewBox="0 0 12 12" aria-hidden="true"><circle cx="6" cy="6" r="6" fill="var(--brand-green)"/></svg>
        euan.brackwell@brackwellconsulting.example
      </li>
    </ul>

    <div class="web-bar">
      <span class="web-bar__url">www.brackwellconsulting.example</span>
    </div>
  </section>

</main>
</body>
</html>
```